The Willowbank Growers Garden Nursery Cards

We are looking for a professional nice business card for the Garden Center. I attached our current cards so you have the information. We do have 2 locations so that is also listed. We like the brown fade in the front, but if you have other ideas that is fine.

Also the back of the card we would like to have the ariel picture of the nursery on the card. I have that picture attached.

I also uploaded our logo files for you.

Target Market(s)

Retail

Industry/Entity Type

Retail Garden Center

Contact Information for Business Card

I have uploaded card samples.

Colors

Designer to choose colors to be used in the design.

Requirements
Must have
• Name, email, phone, cell, locations

```html
<!DOCTYPE html>
<html lang="en">
<head>
<meta charset="utf-8">
<title>The Willowbank Growers – Business Card</title>
<link rel="stylesheet" href="https://fonts.googleapis.com/css2?family=Cinzel:wght@700&family=Arimo:wght@400&display=swap">
<style>
  :root {
    --backdrop: #5a5a5a;
    --card-white: #ffffff;
    --brand-green: #1b4d2c;
    --accent-orange: #f58a1f;
    --text-gray: #555555;
    --rule-gray: #cfcfcf;
    --sun-yellow: #fff200;
    --sun-orange: #fb9a10;
  }
  * { box-sizing: border-box; margin: 0; padding: 0; }
  html, body {
    width: 1200px;
    height: 1200px;
    overflow: hidden;
    background: var(--backdrop);
  }
  .card {
    position: absolute;
    width: 690px;
    height: 394px;
  }
  .card--front {
    left: 266px;
    top: 158px;
    background: var(--card-white);
  }
  .card--back {
    left: 260px;
    top: 651px;
    background: linear-gradient(180deg, var(--sun-yellow) 0%, #fdc60d 50%, var(--sun-orange) 100%);
  }
  .brand-name {
    font-family: "Cinzel", serif;
    font-weight: 700;
    color: var(--brand-green);
    text-transform: uppercase;
  }
  .card--front .brand-name {
    position: absolute;
    right: 46px;
    top: 66px;
    width: 200px;
    text-align: center;
    font-size: 22px;
    line-height: 1.25;
  }
  .card--back .brand-name {
    position: absolute;
    left: 0;
    right: 0;
    top: 150px;
    text-align: center;
    font-size: 38px;
    line-height: 1.25;
  }
  .person-name {
    position: absolute;
    left: 47px;
    top: 226px;
    font-family: "Cinzel", serif;
    font-weight: 700;
    font-size: 27px;
    color: var(--brand-green);
    letter-spacing: 0.5px;
  }
  .person-title {
    position: absolute;
    left: 48px;
    top: 255px;
    font-family: "Arimo", sans-serif;
    font-size: 16px;
    color: var(--accent-orange);
  }
  .divider {
    position: absolute;
    left: 48px;
    top: 281px;
    width: 592px;
    height: 1px;
    background: var(--rule-gray);
  }
  .contact-list {
    position: absolute;
    left: 46px;
    top: 291px;
    list-style: none;
    font-family: "Arimo", sans-serif;
    font-size: 16px;
    color: var(--text-gray);
  }
  .contact-list li {
    display: flex;
    align-items: center;
    height: 20.5px;
  }
  .contact-icon {
    width: 15px;
    height: 15px;
    margin-right: 9px;
    fill: var(--brand-green);
  }
  .address-block {
    position: absolute;
    right: 44px;
    top: 293px;
    text-align: right;
    font-family: "Arimo", sans-serif;
    font-size: 16px;
    line-height: 20.5px;
    color: var(--text-gray);
  }
</style>
</head>
<body>

<section class="card card--front">
  <div class="brand-name">The Willowbank Growers</div>

  <div class="person-name">DALE HARTWELL</div>
  <div class="person-title">General Manager</div>
  <div class="divider"></div>

  <ul class="contact-list">
    <li>
      <svg class="contact-icon" viewBox="0 0 16 16" aria-hidden="true">
        <path d="M3.2 1.2l2.3-.4 1.4 3.4-1.6 1.2c.8 1.8 2.2 3.3 4 4.1l1.3-1.6 3.4 1.4-.4 2.4c-.2.8-.9 1.3-1.7 1.2C6.7 12.4 2.6 8.3 2 3.1c-.1-.8.4-1.6 1.2-1.9z"/>
      </svg>
      555-014-2280 ext 118
    </li>
    <li>
      <svg class="contact-icon" viewBox="0 0 16 16" aria-hidden="true">
        <path d="M4 1h7l1 1v4H4z M1 7h14v6H1z M4 11h8v4H4z" />
      </svg>
      555-014-2291
    </li>
    <li>
      <svg class="contact-icon" viewBox="0 0 16 16" aria-hidden="true">
        <path d="M1 4h14v9H1z" />
        <path d="M1.5 4.5L8 9l6.5-4.5" fill="none" stroke="#ffffff" stroke-width="1.2"/>
      </svg>
      dale@willowbankgrowers.com
    </li>
  </ul>

  <address class="address-block" style="font-style: normal;">
    4120 Orchard Lane Road<br>
    Millbrook. FL. 34100<br>
    willowbankgrowers.com
  </address>
</section>

<section class="card card--back">
  <div class="brand-name">The Willowbank<br>Growers</div>
</section>

</body>
</html>
```